Upsell Vertical Banner Ad Design For B2B Marketing Agency Vertical 768px × 1180px IS THE SIZE

I need a banner made for my website www.brightlanepromotionhub.biz This banner will be an upsell advertisement for after someone signs up for my monthly program. When they login to their account for the 1st time I will give them the chance to upgrade their account to our annual program with just one click.

this is a page that upsells it currently to give you an idea how we market ourselves:
https://tlpx.pagevault-example.com/page/tlp-annual-upsell

Use this content:

Are You Ready To Commit To Taking Your Business To The Next Level?

Because We're In This For The Long-Haul and Dedicated To Your Success...

Save $300 By Upgrading To An Annual Membership And Pay Only $74/mth

((BUTTON))Yes, Upgrade My Plan Right Now!

*Must prepay the full year at only $898/yr!

Target Market(s)

business owners

Industry/Entity Type

Marketing

Requirements
Must have
• 768px × 1180px IS THE SIZE vertical

Use this content:

Nice to have
• Use this content:

Should not have
• Use this content:

```html
<!DOCTYPE html>
<html lang="en">
<head>
<meta charset="utf-8">
<title>Annual Membership Upsell Banner</title>
<link href="https://fonts.googleapis.com/css2?family=Oswald:wght@300;600;700&family=Montserrat:wght@300;500;600;700&family=Syne:wght@800&display=swap" rel="stylesheet">
<style>
  :root{
    --green-dark:#2a7d32;
    --green-light:#4caf50;
    --blue-dark:#0560a3;
    --blue-mid:#0a5ea8;
    --blue-light:#0a7fd6;
    --ink:#2b2b2b;
    --paper:#ffffff;
    --note-bg:#ececec;
    --stage:#e9e9e9;
  }
  *{box-sizing:border-box;margin:0;padding:0}
  html,body{width:1200px;height:1200px;overflow:hidden;background:var(--stage)}
  .banner{
    position:absolute;left:216px;top:10px;width:768px;height:1180px;
    background:linear-gradient(135deg,#f3f3f3 0%,#ffffff 45%,#f6f6f6 100%);
    overflow:hidden;text-align:center;
  }
  .banner p,.banner span{white-space:nowrap}
  .header-shape{position:absolute;left:0;top:0;width:768px;height:390px}
  .headline{font-weight:inherit}
  .headline-top{
    position:absolute;left:0;right:0;top:51px;display:block;
    font-family:"Oswald",sans-serif;font-weight:300;font-size:88px;line-height:1;
    color:var(--paper);letter-spacing:2px;
  }
  .headline-pill{
    position:absolute;left:55px;top:163px;width:657px;height:68px;
    background:var(--paper);border-radius:10px;
    display:flex;align-items:center;justify-content:center;
    font-family:"Oswald",sans-serif;font-weight:700;font-size:37px;line-height:1;
    color:var(--blue-mid);
  }
  .headline-bottom{
    position:absolute;left:0;right:0;top:228px;display:block;
    font-family:"Oswald",sans-serif;font-weight:700;font-size:67px;line-height:1.2;
    color:var(--paper);
  }
  .pledge{position:absolute;left:0;right:0;top:402px;font-family:"Montserrat",sans-serif}
  .pledge-lead{font-size:38px;line-height:56px;letter-spacing:6px;color:var(--ink);font-weight:300}
  .pledge-lead b{color:var(--blue-mid);font-weight:700}
  .pledge-mid{font-size:37px;line-height:52px;font-weight:600;color:var(--ink)}
  .pledge-end{font-size:58px;line-height:70px;font-weight:700;color:var(--blue-mid)}
  .offer{
    position:absolute;left:55px;top:609px;width:657px;height:257px;
    border:1px solid #4c86b8;border-radius:8px;overflow:hidden;
    background:linear-gradient(180deg,#f0f0f0,#fbfbfb);
    box-shadow:0 22px 18px -14px rgba(0,0,0,.28);
  }
  .offer-amount{
    height:147px;background:linear-gradient(90deg,var(--blue-dark),var(--blue-light));
    display:flex;align-items:center;justify-content:center;
    font-family:"Oswald",sans-serif;font-weight:700;font-size:106px;color:var(--paper);
    letter-spacing:1px;padding-top:4px;
  }
  .offer-terms{
    padding-top:20px;font-family:"Syne",sans-serif;font-weight:800;font-size:19px;
    line-height:36px;color:var(--ink);letter-spacing:-0.4px;
  }
  .cta{position:absolute;left:69px;top:909px;width:630px;height:152px}
  .cta-shape{position:absolute;left:0;top:0}
  .cta-label{
    position:absolute;left:0;right:0;top:20px;
    font-family:"Oswald",sans-serif;font-weight:700;font-size:50px;line-height:58px;
    color:var(--paper);
  }
  .note{
    position:absolute;left:60px;top:1101px;width:647px;height:51px;
    background:var(--note-bg);border:1px solid #dcdcdc;border-radius:4px;
    display:flex;align-items:center;justify-content:center;
    font-family:"Montserrat",sans-serif;font-weight:500;font-size:19px;
    letter-spacing:3.6px;color:var(--ink);
  }
</style>
</head>
<body>
<main class="banner">
  <svg class="header-shape" viewBox="0 0 768 390" aria-hidden="true">
    <defs>
      <linearGradient id="greenBand" x1="0" x2="1" y1="0" y2="0">
        <stop offset="0" stop-color="#2a7d32"/>
        <stop offset="1" stop-color="#4caf50"/>
      </linearGradient>
    </defs>
    <polygon points="0,0 768,0 768,330 384,388 0,330" fill="url(#greenBand)"/>
  </svg>
  <h1 class="headline">
    <span class="headline-top">ARE YOU READY</span>
    <span class="headline-pill">TO COMMIT TO TAKING YOUR BUSINESS</span>
    <span class="headline-bottom">TO THE NEXT LEVEL?</span>
  </h1>

  <div class="pledge">
    <p class="pledge-lead"><b>Because</b> We're In This</p>
    <p class="pledge-mid">For The Long-Haul and Dedicated</p>
    <p class="pledge-end">To Your Success...</p>
  </div>

  <section class="offer">
    <div class="offer-amount">SAVE $300</div>
    <p class="offer-terms">By Upgrading To An Annual Membership<br>And Pay Only $74/mth</p>
  </section>

  <div class="cta">
    <svg class="cta-shape" viewBox="0 0 630 152" width="630" height="152" aria-hidden="true">
      <defs>
        <linearGradient id="ctaFill" x1="0" x2="1" y1="0" y2="0">
          <stop offset="0" stop-color="#2a7d32"/>
          <stop offset="1" stop-color="#4caf50"/>
        </linearGradient>
      </defs>
      <polygon points="0,6 6,0 624,0 630,6 617,132 315,150 13,132" fill="#2f8a35"/>
      <polygon points="0,6 6,0 624,0 630,6 618,126 315,144 12,126" fill="url(#ctaFill)"/>
    </svg>
    <p class="cta-label">YES, UPGRADE MY PLAN<br>RIGHT NOW!</p>
  </div>

  <p class="note">*Must prepay the full year at only $898/yr!</p>
</main>
</body>
</html>
```